Fendra corporate branding Powerpoint template*

We are a IT / tech company focussed on no nonsense services for our customers. Our main colors are blue and Orange as seen in the attached logo. Our catchphrase is Simply Fendra. We will use this template for corporate presentations at customers and potential projects.Please make sure the powerpoint does not have any art in there as the standard computers or whatsoever. We want a sleek clean design with our logo and both our colors in a main role.

Target Market(s)

Our existing customers and new customers

Industry/Entity Type

It Company

Colors

Requirements
Must have
• Different slides for different scenarios.
• Look and feel across the entire template
Nice to have
• Enough space to have our own bullet points
Should not have
• To overcrowded slides. Too loud design.

```html
<!DOCTYPE html>
<html lang="en">
<head>
<meta charset="utf-8">
<title>Fendra Presentation Template Overview</title>
<link rel="stylesheet" href="https://fonts.googleapis.com/css2?family=Signika:wght@300;400;600&display=swap">
<style>
:root{
  --blue:#1d4f91;
  --blue-deep:#143b73;
  --orange:#f07a1c;
  --board:#f1f1f3;
  --ink:#2b3f63;
  --muted:#7b8290;
  --line:#d9dde3;
  --card:#f2f3f5;
  --white:#ffffff;
}
*{margin:0;padding:0;box-sizing:border-box}
html,body{width:1200px;height:675px;overflow:hidden}
body{background:var(--board);font-family:"Signika",sans-serif;color:var(--ink);position:relative}
.abs{position:absolute}
.board-title{position:absolute;left:-77px;top:228px;width:200px;transform:rotate(-90deg);font-size:18px;font-weight:600;color:var(--blue);white-space:nowrap;text-align:center}
.spec{position:absolute;left:60px;width:180px;text-align:center;font-weight:600;color:var(--blue-deep)}
.spec-ratio{top:530px;font-size:16px}
.spec-count{top:571px;font-size:16px}
.brand{position:absolute;text-align:center;line-height:1}
.brand-name{display:block;font-weight:600;color:var(--blue)}
.brand-tag{display:block;font-weight:400;color:var(--muted)}
.brand-sm .brand-name{font-size:8px}
.brand-sm .brand-tag{font-size:3.4px;margin-top:1px}
.brand-lg{left:1015px;top:534px;width:120px}
.brand-lg .brand-name{font-size:26px}
.brand-lg .brand-tag{font-size:9px;margin-top:3px}
.slide{position:absolute;width:350px;height:196px;background:var(--white);overflow:hidden;box-shadow:0 1px 4px rgba(0,0,0,.18)}
.row1{top:14px}.row2{top:239px}.row3{top:457px}
.col1{left:51px}.col2{left:425px}.col3{left:799px}
.s7{left:245px}.s8{left:619px}
.strip{position:absolute;left:0;top:0;width:20px;height:196px;background:linear-gradient(180deg,var(--blue) 0%,var(--blue) 35%,var(--orange) 85%)}
.heading{position:absolute;font-size:5.8px;font-weight:600;color:var(--blue-deep)}
.underline{position:absolute;height:1.2px;width:15px;background:var(--orange)}
.body{position:absolute;font-size:3.9px;line-height:10.6px;color:var(--ink);font-weight:300}
.photo{position:absolute}
.social{position:absolute;display:flex;gap:6px}
.social span{width:7px;height:7px;border:.7px solid var(--blue);border-radius:50%}
.cover{background:linear-gradient(160deg,#2d62a8 0%,#5b7fa8 30%,#d9864a 62%,var(--orange) 100%)}
.cover-date{position:absolute;left:22px;top:14px;transform-origin:left top;transform:rotate(-90deg) translateX(-47px);font-size:3.6px;letter-spacing:1.2px;color:var(--white);white-space:nowrap}
.cover-rule{position:absolute;left:26px;top:72px;width:.8px;height:124px;background:var(--white)}
.cover-kicker{position:absolute;left:55px;top:43px;font-size:7px;color:var(--white)}
.cover-title{position:absolute;left:55px;top:80px;font-size:13.5px;line-height:24px;font-weight:600;color:var(--blue)}
.presenter{position:absolute;left:81px;top:153px;font-size:4.6px;line-height:9px;color:#fde4cf}
.svc{position:absolute;width:130px}
.svc h4{font-size:5.2px;font-weight:600;color:var(--blue-deep);margin-bottom:3px}
.svc p{font-size:3.9px;line-height:8.4px;font-weight:300;width:100px}
.svc svg{position:absolute;left:-12px;top:-1px}
.why{position:absolute;width:90px;text-align:center}
.why h4{font-size:6px;font-weight:600;color:var(--blue-deep);margin:8px 0 5px}
.why p{font-size:4px;line-height:8.4px;font-weight:300;width:66px;margin:0 auto}
.contact-card{position:absolute;left:222px;top:37px;width:101px;height:135px;background:var(--card)}
.contact-item{position:absolute;left:23px;font-size:3.7px;line-height:7.8px;color:var(--muted)}
.contact-item svg{position:absolute;left:-9px;top:0}
</style>
</head>
<body>

<div class="board-title">PowerPoint Presentation</div>
<div class="spec spec-ratio">Aspect Ratio - 16:9</div>
<div class="spec spec-count">8 slides</div>
<div class="brand brand-lg"><span class="brand-name">Fendra</span><span class="brand-tag">Simply Fendra</span></div>

<section class="slide cover row1 col1">
  <div class="photo" role="img" aria-label="Illustration of a hooded figure at a laptop" style="left:270px;top:68px;width:40px;height:62px;border-radius:10px;background:rgba(255,255,255,.18)"></div>
  <div class="cover-date">November 2019</div>
  <div class="cover-rule"></div>
  <div class="cover-kicker">Sales and Consultancy</div>
  <div class="cover-title">Information Technology<br>Company</div>
  <div class="photo" role="img" aria-label="Portrait of the presenter" style="left:45px;top:143px;width:30px;height:30px;border-radius:50%;background:linear-gradient(#e9e9ea,#b9bcc2);border:1px solid #fff"></div>
  <div class="presenter">Presented by: Mara Lindqvist<br>Marketing Director</div>
  <div class="brand brand-sm" style="left:274px;top:157px;width:54px"><span class="brand-name" style="font-size:11px">Fendra</span><span class="brand-tag" style="font-size:4px;color:#fde4cf">Simply Fendra</span></div>
</section>

<section class="slide row1 col2">
  <div class="photo" role="img" aria-label="Photo of a desk with a laptop and plants by a window" style="left:0;top:0;width:350px;height:78px;background:linear-gradient(90deg,#b9c7a0,#e3e6de 45%,#cfd7c0)"></div>
  <div class="abs" style="left:0;top:78px;width:15px;height:118px;background:linear-gradient(180deg,var(--blue),var(--orange))"></div>
  <div class="photo" role="img" aria-label="Portrait of the founder" style="left:145px;top:47px;width:60px;height:60px;border-radius:50%;background:linear-gradient(#eceded,#c7c9cd);border:1.5px solid #fff"></div>
  <div class="social" style="left:4px;top:151px;flex-direction:column;gap:5px"><span style="border-color:#fff"></span><span style="border-color:#fff"></span><span style="border-color:#fff"></span></div>
  <div class="heading" style="left:0;width:350px;text-align:center;top:121px">Welcome Message</div>
  <div class="abs" style="left:70px;top:140px;font-size:11px;font-weight:600;color:var(--blue-deep)">&ldquo;</div>
  <div class="body" style="left:85px;width:180px;top:143px;text-align:center;color:var(--muted)">Presentations are communication tools that can be used as demonstrations, lectures, speeches, reports, and more. Most of the time, they’re presented before an audience.</div>
  <div class="abs" style="left:267px;top:155px;font-size:11px;font-weight:600;color:var(--blue-deep)">&rdquo;</div>
  <div class="abs" style="left:0;width:350px;text-align:center;top:175px;font-size:4.6px;font-style:italic;color:var(--blue-deep)">Owen Hale</div>
  <div class="abs" style="left:0;width:350px;text-align:center;top:184px;font-size:4px;font-style:italic;color:var(--muted)">Founder &amp; Chairman</div>
  <div class="brand brand-sm" style="left:300px;top:179px;width:38px"><span class="brand-name">Fendra</span><span class="brand-tag">Simply Fendra</span></div>
</section>

<section class="slide row1 col3">
  <div class="strip"></div>
  <div class="photo" role="img" aria-label="Photo of a bright white workspace with a desktop computer" style="left:204px;top:0;width:146px;height:196px;background:linear-gradient(180deg,#f6f6f6,#e9e7e4 60%,#d9d3cc)"></div>
  <div class="brand brand-sm" style="left:304px;top:8px;width:38px"><span class="brand-name">Fendra</span><span class="brand-tag">Simply Fendra</span></div>
  <div class="heading" style="left:54px;top:37px">About Us</div>
  <div class="underline" style="left:54px;top:49px"></div>
  <div class="body" style="left:54px;top:61px;width:118px">Presentations are communication tools that can be used as demonstrations, lectures, speeches, reports, and more. Most of the time, they’re presented before an audience.</div>
  <div class="abs" style="left:54px;top:95px;width:113px;height:.5px;background:var(--line)"></div>
  <div class="body" style="left:54px;top:102px;width:118px">Presentations are communication tools that can be used as demonstrations, lectures, speeches, reports, and more. Most of the time, they’re presented before an audience.</div>
  <div class="abs" style="left:54px;top:138px;width:113px;height:.5px;background:var(--line)"></div>
  <div class="body" style="left:54px;top:149px;width:118px">Presentations are communication tools that can be used as demonstrations, lectures, speeches, reports, and more. Most of the time, they’re presented before an audience.</div>
</section>

<section class="slide row2 col1">
  <div class="strip"></div>
  <div class="brand brand-sm" style="left:304px;top:8px;width:38px"><span class="brand-name">Fendra</span><span class="brand-tag">Simply Fendra</span></div>
  <div class="heading" style="left:0;width:350px;text-align:center;top:14px">The Team</div>
  <div class="underline" style="left:168px;top:25px"></div>
  <div class="abs" style="left:127px;top:56px;width:.5px;height:116px;background:var(--line)"></div>
  <div class="abs" style="left:223px;top:56px;width:.5px;height:116px;background:var(--line)"></div>

  <div class="photo" role="img" aria-label="Portrait of the founder" style="left:55px;top:58px;width:50px;height:50px;border-radius:50%;background:linear-gradient(#ececec,#c5c7cb)"></div>
  <div class="abs" style="left:30px;width:100px;text-align:center;top:114px;font-size:5px;font-weight:600;color:var(--blue-deep)">Owen Hale</div>
  <div class="abs" style="left:30px;width:100px;text-align:center;top:123px;font-size:4px;font-style:italic">Founder</div>
  <div class="social" style="left:62px;top:137px"><span></span><span></span><span></span></div>
  <div class="body" style="left:45px;width:70px;top:151px;text-align:center;font-size:3.3px;line-height:6px">Presentations are communication tools that can be used as demonstrations, lectures, speeches, reports, and more.</div>

  <div class="photo" role="img" aria-label="Portrait of the lead developer" style="left:150px;top:58px;width:50px;height:50px;border-radius:50%;background:linear-gradient(#eae7e6,#b9a5a5)"></div>
  <div class="abs" style="left:125px;width:100px;text-align:center;top:114px;font-size:5px;font-weight:600;color:var(--blue-deep)">Nadia Verhoef</div>
  <div class="abs" style="left:125px;width:100px;text-align:center;top:123px;font-size:4px;font-style:italic">Lead Developer</div>
  <div class="social" style="left:157px;top:137px"><span></span><span></span><span></span></div>
  <div class="body" style="left:140px;width:70px;top:151px;text-align:center;font-size:3.3px;line-height:6px">Presentations are communication tools that can be used as demonstrations, lectures, speeches, reports, and more.</div>

  <div class="photo" role="img" aria-label="Portrait of the lead developer" style="left:245px;top:58px;width:50px;height:50px;border-radius:50%;background:linear-gradient(#eeeeee,#c2c4c8)"></div>
  <div class="abs" style="left:220px;width:100px;text-align:center;top:114px;font-size:5px;font-weight:600;color:var(--blue-deep)">Ravi Okoro</div>
  <div class="abs" style="left:220px;width:100px;text-align:center;top:123px;font-size:4px;font-style:italic">Lead Developer</div>
  <div class="social" style="left:252px;top:137px"><span></span><span></span><span></span></div>
  <div class="body" style="left:235px;width:70px;top:151px;text-align:center;font-size:3.3px;line-height:6px">Presentations are communication tools that can be used as demonstrations, lectures, speeches, reports, and more.</div>
</section>

<section class="slide row2 col2">
  <div class="abs" style="left:80px;top:16px;width:64px;height:163px;border:1px solid var(--blue)"></div>
  <div class="photo" role="img" aria-label="Photo of a laptop on a windowsill" style="left:0;top:29px;width:120px;height:137px;background:linear-gradient(160deg,#c8d3b6,#eef0ec 50%,#b9b1a6)"></div>
  <div class="brand brand-sm" style="left:304px;top:8px;width:38px"><span class="brand-name">Fendra</span><span class="brand-tag">Simply Fendra</span></div>
  <div class="heading" style="left:177px;top:52px">Company Mission/ Vision</div>
  <div class="underline" style="left:177px;top:64px"></div>
  <div class="body" style="left:177px;top:74px;width:128px;line-height:11.3px">Presentations are communication tools that can be used as demonstrations, lectures, speeches, reports, and more. Most of the time, they’re presented before an audience.</div>
  <div class="body" style="left:177px;top:120px;width:128px;line-height:11.3px">It serves a variety of purposes, making them powerful tools for convincing and teaching.</div>
</section>

<section class="slide row2 col3">
  <div class="photo" role="img" aria-label="Photo of colleagues talking in an office, blue tinted" style="left:0;top:0;width:350px;height:62px;background:linear-gradient(90deg,#4f73a6,#7b98c3 50%,#3f659b)"></div>
  <div class="abs" style="left:3px;top:2px;width:344px;height:58px;border:.5px solid rgba(255,255,255,.6)"></div>
  <div class="abs" style="left:0;width:350px;text-align:center;top:24px;font-size:5.4px;color:#fff">Our Services</div>
  <div class="underline" style="left:168px;top:35px"></div>

  <div class="svc" style="left:30px;top:78px"><svg width="9" height="7" viewBox="0 0 9 7"><path d="M2 6.5h5a1.8 1.8 0 0 0 0-3.6A2.5 2.5 0 0 0 2.2 3 1.7 1.7 0 0 0 2 6.5z" fill="none" stroke="#1d4f91" stroke-width=".5"/></svg><h4>Cloud Computing</h4><p>It serves a variety of purposes, making them powerful tools for convincing and teaching.</p></div>
  <div class="svc" style="left:30px;top:116px"><svg width="8" height="8" viewBox="0 0 8 8"><path d="M1 7l5-5M2 1l5 5M5 1h2v2" fill="none" stroke="#1d4f91" stroke-width=".8"/></svg><h4>IT Infrastructure</h4><p>It serves a variety of purposes, making them powerful tools for convincing and teaching.</p></div>
  <div class="svc" style="left:30px;top:153px"><svg width="9" height="8" viewBox="0 0 9 8"><rect x=".5" y="1" width="8" height="6.5" fill="none" stroke="#1d4f91" stroke-width=".5"/><path d="M.5 4h8" stroke="#1d4f91" stroke-width=".5"/></svg><h4>Endpoint Management</h4><p>It serves a variety of purposes, making them powerful tools for convincing and teaching.</p></div>

  <div class="svc" style="left:192px;top:75px"><svg width="9" height="8" viewBox="0 0 9 8"><path d="M.5 3L2 .5h5L8.5 3v4.5h-8z M.5 3h8" fill="none" stroke="#1d4f91" stroke-width=".5"/></svg><h4>Custom Software</h4><p>It serves a variety of purposes, making them powerful tools for convincing and teaching.</p></div>
  <div class="svc" style="left:192px;top:113px"><svg width="8" height="9" viewBox="0 0 8 9"><circle cx="4" cy="3.5" r="3" fill="#1d4f91"/><rect x="2.5" y="6" width="3" height="2.5" fill="#1d4f91"/></svg><h4>IT Consultancy</h4><p>It serves a variety of purposes, making them powerful tools for convincing and teaching.</p></div>
  <div class="svc" style="left:192px;top:150px"><svg width="9" height="7" viewBox="0 0 9 7"><rect x=".5" y=".5" width="8" height="6" fill="none" stroke="#1d4f91" stroke-width=".5"/><path d="M.5.5l4 3.3 4-3.3" fill="none" stroke="#1d4f91" stroke-width=".5"/></svg><h4>Email Marketing</h4><p>It serves a variety of purposes, making them powerful tools for convincing and teaching.</p></div>
  <div class="brand brand-sm" style="left:299px;top:180px;width:38px"><span class="brand-name">Fendra</span><span class="brand-tag">Simply Fendra</span></div>
</section>

<section class="slide row3 s7">
  <div class="photo" role="img" aria-label="Faded photo of a smiling team" style="left:0;top:40px;width:350px;height:156px;background:linear-gradient(90deg,#f4f5f7,#e7e9ec 40%,#eef0f2 60%,#e4e6ea)"></div>
  <div class="brand brand-sm" style="left:7px;top:7px;width:38px"><span class="brand-name">Fendra</span><span class="brand-tag">Simply Fendra</span></div>
  <div class="heading" style="left:0;width:350px;text-align:center;top:23px">Why Choose Us</div>
  <div class="underline" style="left:168px;top:37px"></div>
  <div class="abs" style="left:132px;top:60px;width:85px;height:110px;background:#f2f3f5;border:.5px solid #dde0e4;border-radius:2px;box-shadow:0 1px 3px rgba(0,0,0,.12)"></div>
  <div class="why" style="left:18px;top:84px"><svg width="22" height="14" viewBox="0 0 22 14"><path d="M1 6l5-4 5 3 5-3 5 4-6 6-4-3-4 3z" fill="#1d4f91"/></svg><h4>Professional</h4><p>It serves a variety of purposes, making them powerful tools for convincing and teaching.</p></div>
  <div class="why" style="left:129px;top:82px"><svg width="14" height="18" viewBox="0 0 14 18"><rect x="1" y="1" width="12" height="16" fill="none" stroke="#1d4f91" stroke-width="1"/><path d="M3 5h2M7 5h4M3 9h2M7 9h4M3 13h2M7 13h4" stroke="#1d4f91" stroke-width="1"/></svg><h4>Quality</h4><p>It serves a variety of purposes, making them powerful tools for convincing and teaching.</p></div>
  <div class="why" style="left:250px;top:84px"><svg width="24" height="14" viewBox="0 0 24 14"><circle cx="5" cy="4" r="2.5" fill="#1d4f91"/><circle cx="12" cy="3" r="3" fill="#1d4f91"/><circle cx="19" cy="4" r="2.5" fill="#1d4f91"/><path d="M1 13a4 4 0 0 1 8 0zM7 13a5 5 0 0 1 10 0zM15 13a4 4 0 0 1 8 0z" fill="#1d4f91"/></svg><h4>Experienced</h4><p>It serves a variety of purposes, making them powerful tools for convincing and teaching.</p></div>
</section>

<section class="slide row3 s8">
  <div class="brand brand-sm" style="left:7px;top:7px;width:38px"><span class="brand-name">Fendra</span><span class="brand-tag">Simply Fendra</span></div>
  <div class="heading" style="left:16px;top:82px">Contact Us</div>
  <div class="underline" style="left:16px;top:93px"></div>
  <div class="body" style="left:16px;top:98px;width:94px;color:var(--muted)">Presentations are communication tools that can be used as demonstrations, lectures, speeches, reports, and more. Most of the time, they’re presented before an audience.</div>
  <div class="photo" role="img" aria-label="Illustration of a glowing network globe with connected device icons" style="left:119px;top:0;width:132px;height:196px;background:radial-gradient(circle at 60% 50%,#4d79c9,#1a3f8f 55%,#0d2560)"></div>
  <div class="contact-card">
    <div class="heading" style="left:13px;top:8px;font-size:5.2px">Get in Touch</div>
    <div class="contact-item" style="top:21px"><svg width="6" height="8" viewBox="0 0 6 8"><path d="M3 7.5S.5 4.5.5 3a2.5 2.5 0 0 1 5 0C5.5 4.5 3 7.5 3 7.5z" fill="none" stroke="#1d4f91" stroke-width=".5"/><circle cx="3" cy="3" r=".9" fill="#1d4f91"/></svg>88 Harbour Lane<br>Eastfield, Westshire 20418<br>United Kingdom</div>
    <div class="contact-item" style="top:48px"><svg width="6" height="6" viewBox="0 0 6 6"><path d="M1 .5l1.2 1.6-.6.8a3.5 3.5 0 0 0 1.5 1.5l.8-.6L5.5 5 4.7 5.7C2.5 5.5.5 3.5.3 1.3z" fill="none" stroke="#1d4f91" stroke-width=".5"/></svg>+31 204 55 17</div>
    <div class="contact-item" style="top:64px"><svg width="7" height="5" viewBox="0 0 7 5"><rect x=".3" y=".3" width="6.4" height="4.4" fill="none" stroke="#1d4f91" stroke-width=".5"/><path d="M.3.3l3.2 2.5L6.7.3" fill="none" stroke="#1d4f91" stroke-width=".5"/></svg>hello@fendra-it.com</div>
    <div class="contact-item" style="top:83px"><svg width="7" height="7" viewBox="0 0 7 7"><circle cx="3.5" cy="3.5" r="3" fill="none" stroke="#1d4f91" stroke-width=".5"/><path d="M.5 3.5h6M3.5.5c-1.6 2-1.6 4 0 6M3.5.5c1.6 2 1.6 4 0 6" fill="none" stroke="#1d4f91" stroke-width=".4"/></svg>www.fendra-it.com</div>
    <div class="contact-item" style="top:102px"><svg width="6" height="6" viewBox="0 0 6 6"><circle cx="3" cy="3" r="2.7" fill="none" stroke="#1d4f91" stroke-width=".5"/></svg>Fendra IT</div>
    <div class="contact-item" style="top:122px"><svg width="6" height="6" viewBox="0 0 6 6"><circle cx="3" cy="3" r="2.7" fill="none" stroke="#1d4f91" stroke-width=".5"/></svg>@fendra.it</div>
  </div>
</section>

</body>
</html>
```